Looking for an attractive, cool poster design for our company Core Values. This would ideally be framed and placed at each company location. Would like this to be striking and memorable.

The core values that should be included on the poster are:

Be a Creator
Have an Open Mind
Do the Right Thing

The size should be standard poster size, 18 x 24, vertical orientation ideally.

The company name to include on the poster is:

Brightwater Systems Group

The design could be printed as a poster or a sticker/decal as well. Or perhaps printed on a fabric, foam boards. Versatile enough design for different output types.

Target Market(s)

Internal Team Members and visitors

Industry/Entity Type

Technology

Font styles to use
Other font styles liked:
• Montserrat

Requirements
Must have
• The design could be printed as a poster or a sticker/decal as well. Or perhaps printed on a fabric. Versatile enough design for different output types.

```html
<!DOCTYPE html>
<html lang="en">
<head>
<meta charset="utf-8">
<title>Core Values Poster – Brightwater Systems Group</title>
<link href="https://fonts.googleapis.com/css2?family=Montserrat:wght@700;800&family=Playfair+Display:ital,wght@1,700&family=Roboto+Slab:wght@700&family=Anton&display=swap" rel="stylesheet">
<style>
  :root {
    --backdrop: #0d3559;
    --paper: #f1f1f0;
    --navy: #0f3a61;
    --orange: #de8222;
    --white: #ffffff;
  }
  html, body {
    margin: 0;
    padding: 0;
    width: 1200px;
    height: 900px;
    overflow: hidden;
    background: var(--backdrop);
  }
  .poster {
    position: absolute;
    left: 297px;
    top: 20px;
    width: 605px;
    height: 860px;
    background: var(--paper);
  }
  .poster svg { display: block; width: 100%; height: 100%; }
  .sans { font-family: "Montserrat", sans-serif; }
  .script { font-family: "Playfair Display", serif; font-style: italic; font-weight: 700; }
  .slab { font-family: "Roboto Slab", serif; font-weight: 700; }
  .condensed { font-family: "Anton", sans-serif; }
  .fill-navy { fill: var(--navy); }
  .fill-orange { fill: var(--orange); }
  .fill-white { fill: var(--white); }
</style>
</head>
<body>
<main class="poster">
  <svg viewBox="0 0 605 860" xmlns="http://www.w3.org/2000/svg">
    <!-- border -->
    <rect class="poster-frame" x="28" y="32" width="549" height="794" fill="none" stroke="var(--orange)" stroke-width="4"/>

    <!-- heading ribbon -->
    <g class="heading-ribbon">
      <polygon class="fill-navy" points="67,160 100,148 112,188 92,203"/>
      <polygon class="fill-navy" points="538,160 505,148 493,188 513,203"/>
      <path d="M 88 170 Q 302 28 517 170" fill="none" stroke="var(--navy)" stroke-width="48"/>
      <path d="M 76 152 Q 302 8 529 152" fill="none" stroke="var(--white)" stroke-width="1.2" stroke-dasharray="4 3"/>
      <path d="M 100 188 Q 302 48 505 188" fill="none" stroke="var(--white)" stroke-width="1.2" stroke-dasharray="4 3"/>
      <path id="ribbon-line" d="M 88 181 Q 302 39 517 181" fill="none"/>
      <text class="sans fill-orange" font-weight="800" font-size="34" letter-spacing="1">
        <textPath href="#ribbon-line" startOffset="50%" text-anchor="middle">CORE VALUES</textPath>
      </text>
      <text class="fill-white" font-size="16" x="120" y="169" text-anchor="middle">★</text>
      <text class="fill-white" font-size="16" x="485" y="169" text-anchor="middle">★</text>
    </g>

    <!-- company name -->
    <g class="company-name">
      <circle class="fill-navy" cx="302" cy="160" r="12"/>
      <text class="sans fill-navy" font-weight="800" font-size="9" x="302" y="186" text-anchor="middle">BRIGHTWATER SYSTEMS GROUP</text>
    </g>

    <!-- value 1 -->
    <g class="value value-creator">
      <g class="speed-lines" stroke="var(--navy)">
        <line x1="100" y1="246" x2="197" y2="246" stroke-width="1.5"/>
        <line x1="125" y1="252" x2="197" y2="252" stroke-width="2.5"/>
        <line x1="145" y1="258" x2="197" y2="258" stroke-width="1.5"/>
        <line x1="404" y1="246" x2="502" y2="246" stroke-width="1.5"/>
        <line x1="404" y1="252" x2="478" y2="252" stroke-width="2.5"/>
        <line x1="404" y1="258" x2="458" y2="258" stroke-width="1.5"/>
      </g>
      <text class="sans fill-orange" font-weight="800" font-size="96" x="203" y="275" textLength="195" lengthAdjust="spacingAndGlyphs">be a</text>
      <text class="sans fill-navy" font-weight="800" font-size="110" x="69" y="369" textLength="462" lengthAdjust="spacingAndGlyphs">CREATOR</text>
    </g>

    <g class="divider" stroke="var(--navy)" stroke-width="1.2" stroke-dasharray="4 3">
      <line x1="69" y1="384" x2="526" y2="384"/>
      <line x1="69" y1="393" x2="526" y2="393"/>
    </g>

    <!-- value 2 -->
    <g class="value value-open-mind">
      <text class="fill-navy" font-size="20" x="111" y="462" text-anchor="middle">★</text>
      <text class="fill-navy" font-size="20" x="484" y="462" text-anchor="middle">★</text>
      <text class="script fill-orange" font-size="96" x="139" y="479" textLength="321" lengthAdjust="spacingAndGlyphs">have an</text>
      <text class="slab fill-navy" font-size="80" x="69" y="558" textLength="461" lengthAdjust="spacingAndGlyphs">OPEN MIND</text>
    </g>

    <g class="divider" stroke="var(--navy)" stroke-width="1.2" stroke-dasharray="4 3">
      <line x1="69" y1="582" x2="526" y2="582"/>
      <line x1="69" y1="591" x2="526" y2="591"/>
    </g>

    <!-- value 3 -->
    <g class="value value-right-thing">
      <g class="speed-lines" stroke="var(--navy)">
        <line x1="92" y1="660" x2="134" y2="660" stroke-width="1.5"/>
        <line x1="104" y1="666" x2="134" y2="666" stroke-width="2.5"/>
        <line x1="114" y1="672" x2="134" y2="672" stroke-width="1.5"/>
        <line x1="468" y1="660" x2="510" y2="660" stroke-width="1.5"/>
        <line x1="468" y1="666" x2="498" y2="666" stroke-width="2.5"/>
        <line x1="468" y1="672" x2="488" y2="672" stroke-width="1.5"/>
      </g>
      <text class="sans fill-orange" font-weight="800" font-size="96" x="148" y="683" textLength="62" lengthAdjust="spacingAndGlyphs">d</text>
      <g class="tick-o">
        <circle cx="240" cy="657" r="26" fill="none" stroke="var(--orange)" stroke-width="13"/>
        <path d="M 226 656 L 238 670 L 262 637" fill="none" stroke="var(--navy)" stroke-width="9" stroke-linecap="round" stroke-linejoin="round"/>
      </g>
      <text class="sans fill-orange" font-weight="800" font-size="96" x="298" y="683" textLength="155" lengthAdjust="spacingAndGlyphs">the</text>
      <text class="condensed fill-navy" font-size="96" x="72" y="781" textLength="450" lengthAdjust="spacingAndGlyphs">RIGHT THING</text>
    </g>
  </svg>
</main>
</body>
</html>
```